Valoran Real Estate Agency Business Card Design

Hello again, I'd like for you to design our new business cards and letterhead if you can. The cards will be printed on a white/off-white thick card stock. I wanted the color version of the logo alone on one side (possibly with our website URL and maybe the words Residential & Commercial Sales & Leasing), and the below info (listed in business card details) for the other side (or you choose whatever sides look best because I trust your judgement).

Target Market(s)

Property owners, property management companies, buyers & sellers of real estate property

Industry/Entity Type

Real Estate

Contact Information for Business Card

Personal Info:
Peter Dunwell
Licensed Real Estate Broker
Mobile: (212) 555-0143
pdunwell@valoran-example.com

Company Info:
Valoran Agency LLC
48-12 Larkin Avenue, 3FL
Long Island City, NY 11199
www.valoran-example.com
Office: (718) 555-0187

Of course the personal info should be editable so I can order cards for other agents in the future.

Let me know if you have any questions. Looking forward to seeing your ideas.

Requirements
Nice to have
• Some red elements to match the logo but not much
Should not have
• Not too busy, I would like a minimal but professional look.

```html
<!DOCTYPE html>
<html lang="en">
<head>
<meta charset="UTF-8">
<title>Valoran Agency — Business Card</title>
<link rel="stylesheet" href="https://fonts.googleapis.com/css2?family=Arimo:wght@400&display=swap">
<style>
  :root {
    --page-bg: #ffffff;
    --card-bg: #ffffff;
    --ink: #111111;
    --name-ink: #333333;
    --brand-red: #ec1f28;
    --on-red: #ffffff;
    --card-shadow: rgba(0, 0, 0, 0.45);
  }
  * { margin: 0; padding: 0; box-sizing: border-box; }
  html, body {
    width: 1200px;
    height: 849px;
    overflow: hidden;
    background: var(--page-bg);
    font-family: "Arimo", Arial, sans-serif;
    color: var(--ink);
  }
  .canvas { position: relative; width: 1200px; height: 849px; }

  .card {
    position: absolute;
    left: 343px;
    width: 479px;
    height: 266px;
    background: var(--card-bg);
    box-shadow: 2px 3px 3px var(--card-shadow);
    overflow: hidden;
  }
  .card--front { top: 152px; }
  .card--back { top: 450px; height: 264px; }

  .company-label {
    font-family: "Arimo", Arial, sans-serif;
    font-weight: 400;
    color: var(--name-ink);
    line-height: 1;
    white-space: nowrap;
  }
  .card--front .company-label {
    position: absolute;
    left: 28px;
    top: 16px;
    font-size: 22px;
  }

  .agent {
    position: absolute;
    left: 28px;
    top: 106px;
    width: 218px;
  }
  .agent__name { font-size: 17px; line-height: 24px; }
  .agent__title { font-size: 15px; line-height: 26px; }
  .agent__line { font-size: 15px; line-height: 26px; display: flex; align-items: center; gap: 4px; }
  .agent__email { font-size: 13.5px; line-height: 28px; white-space: nowrap; }

  .company-panel {
    position: absolute;
    left: 248px;
    top: 0;
    width: 231px;
    height: 100%;
    background: var(--brand-red);
    color: var(--on-red);
    text-align: right;
    padding: 104px 39px 0 0;
  }
  .company__name { font-size: 17px; line-height: 26px; }
  .company__line { font-size: 13.5px; line-height: 25px; white-space: nowrap; }
  .company__phone { display: flex; justify-content: flex-end; align-items: center; gap: 4px; }

  .card--back .company-label {
    position: absolute;
    left: 0;
    right: 0;
    top: 109px;
    text-align: center;
    font-size: 44px;
  }
  .back__url {
    position: absolute;
    left: 0;
    right: 0;
    top: 212px;
    text-align: center;
    font-size: 26px;
    line-height: 30px;
  }
</style>
</head>
<body>
<main class="canvas">

  <section class="card card--front" aria-label="Business card front">
    <p class="company-label">Valoran</p>

    <div class="agent">
      <p class="agent__name">Peter Dunwell</p>
      <p class="agent__title">Licensed Real Estate Broker</p>
      <p class="agent__line">
        <svg width="11" height="15" viewBox="0 0 11 15" aria-hidden="true">
          <rect x="1" y="1" width="9" height="13" rx="1.5" fill="none" stroke="currentColor" stroke-width="1.5"/>
          <line x1="4" y1="11.5" x2="7" y2="11.5" stroke="currentColor" stroke-width="1"/>
        </svg>
        (212) 555-0143
      </p>
      <p class="agent__email">pdunwell@valoran-example.com</p>
    </div>

    <div class="company-panel">
      <p class="company__name">Valoran Agency LLC</p>
      <p class="company__line">48-12 Larkin Avenue, 3FL</p>
      <p class="company__line">Long Island City, NY 11199</p>
      <p class="company__line company__phone">
        <svg width="10" height="12" viewBox="0 0 24 24" aria-hidden="true">
          <path fill="currentColor" d="M6.6 10.8a15.1 15.1 0 0 0 6.6 6.6l2.2-2.2a1 1 0 0 1 1-.25 11.4 11.4 0 0 0 3.6.57 1 1 0 0 1 1 1V20a1 1 0 0 1-1 1A17 17 0 0 1 3 4a1 1 0 0 1 1-1h3.5a1 1 0 0 1 1 1c0 1.25.2 2.45.57 3.57a1 1 0 0 1-.25 1z"/>
        </svg>
        (718) 555-0187
      </p>
    </div>
  </section>

  <section class="card card--back" aria-label="Business card back">
    <p class="company-label">Valoran</p>
    <p class="back__url">www.valoran-example.com</p>
  </section>

</main>
</body>
</html>
```